KALVERIA Consultancy Business Card

We need a business card design for a new Image & Etiquette Consultancy Company.

The design should reflect the corporate colour found in the logo attached.

Info to include:

Name: Melba Tran
Title: Image Consultant
Company: KAL VERIA CONSULTANCY
Address: 27 Kelso Street, #14-09 Harbourline Tower, Singapore 058217
Contact: 9317 6284
Email: melba@kalveria.com.sg
Website: www.kalveria.com.sg

```html
<!DOCTYPE html>
<html lang="en">
<head>
<meta charset="utf-8">
<title>KALVERIA Consultancy – Business Card</title>
<link rel="stylesheet" href="https://fonts.googleapis.com/css2?family=Montserrat:wght@400;500;600&display=swap">
<style>
  :root {
    --backdrop: #e8e8ea;
    --plum: #3f2a56;
    --gold: #c9a24a;
    --paper: #ffffff;
    --ink: #2e2340;
  }
  * { box-sizing: border-box; margin: 0; padding: 0; }
  html, body { width: 1200px; height: 885px; overflow: hidden; }
  body {
    background: var(--backdrop);
    position: relative;
    font-family: "Montserrat", sans-serif;
  }
  .card {
    position: absolute;
    top: 294px;
    width: 520px;
    height: 297px;
    overflow: hidden;
  }
  .card--front { left: 60px; background: var(--plum); }
  .card--back { left: 620px; background: var(--paper); }

  /* front */
  .wordmark {
    position: absolute;
    left: 0; right: 0;
    top: 126px;
    text-align: center;
    font-weight: 500;
    font-size: 40px;
    letter-spacing: 5px;
    color: var(--gold);
    line-height: 1;
  }

  /* back */
  .social { position: absolute; right: 0; top: 0; width: 150px; height: 90px; }
  .back-logo {
    position: absolute;
    left: 24px; top: 100px;
    font-weight: 500;
    font-size: 26px;
    letter-spacing: 3px;
    color: var(--plum);
    line-height: 1;
  }
  .band { position: absolute; left: 0; top: 100px; width: 520px; height: 100px; }
  .name-block {
    position: absolute;
    left: 22px; top: 149px;
    color: var(--paper);
  }
  .name { font-size: 15px; font-weight: 600; letter-spacing: 1.5px; line-height: 1.2; }
  .role { font-size: 8.5px; font-weight: 500; letter-spacing: 1.5px; margin-top: 4px; text-transform: uppercase; }

  .contact { position: absolute; list-style: none; }
  .contact li {
    display: flex; align-items: flex-start; gap: 9px;
    font-size: 11px; color: var(--ink); line-height: 1.35;
    margin-bottom: 7px;
  }
  .contact svg { flex: 0 0 15px; width: 15px; height: 15px; }
  .contact--personal { left: 24px; top: 208px; }
  .contact--online { left: 300px; top: 160px; }
</style>
</head>
<body>

<section class="card card--front" aria-label="Card front">
  <div class="wordmark">KALVERIA</div>
</section>

<section class="card card--back" aria-label="Card back">
  <svg class="social" viewBox="0 0 150 90" aria-label="Social links">
    <g stroke="var(--plum)" stroke-width="1.5" fill="none">
      <path d="M38 52 V10 H60"/>
      <path d="M78 62 V24 H100"/>
      <path d="M118 72 V38 H150"/>
    </g>
    <g fill="var(--plum)">
      <circle cx="60" cy="10" r="3"/>
      <circle cx="100" cy="24" r="3"/>
      <circle cx="38" cy="56" r="10"/>
      <circle cx="78" cy="66" r="10"/>
      <circle cx="118" cy="76" r="10"/>
    </g>
  </svg>

  <div class="back-logo">KALVERIA</div>

  <svg class="band" viewBox="0 0 520 100" aria-hidden="true">
    <g fill="var(--gold)">
      <polygon points="262,38 282,38 304,2 284,2"/>
      <polygon points="288,38 308,38 330,2 310,2"/>
      <polygon points="314,38 334,38 356,2 336,2"/>
    </g>
    <polygon points="0,38 520,38 520,47 270,47 250,90 0,90" fill="var(--plum)"/>
  </svg>

  <div class="name-block">
    <div class="name">MELBA TRAN</div>
    <div class="role">Image Consultant</div>
  </div>

  <ul class="contact contact--personal">
    <li>
      <svg viewBox="0 0 16 16" aria-hidden="true"><circle cx="8" cy="8" r="8" fill="var(--plum)"/><path d="M5.6 4.2l1.3 1.6-.7 1c.5 1 1.3 1.8 2.2 2.3l1-.7 1.6 1.3-.8 1.3c-2.6-.4-4.7-2.5-5-5.1z" fill="#fff"/></svg>
      9317 6284
    </li>
    <li>
      <svg viewBox="0 0 16 16" aria-hidden="true"><circle cx="8" cy="8" r="8" fill="var(--plum)"/><rect x="4.5" y="6" width="7" height="5" rx="1" fill="#fff"/><rect x="6" y="4" width="4" height="2.5" fill="#fff"/></svg>
      6734 2190
    </li>
    <li>
      <svg viewBox="0 0 16 16" aria-hidden="true"><circle cx="8" cy="8" r="8" fill="var(--plum)"/><path d="M8 3.5a3 3 0 0 1 3 3c0 2.2-3 5.8-3 5.8S5 8.7 5 6.5a3 3 0 0 1 3-3z" fill="#fff"/><circle cx="8" cy="6.5" r="1.1" fill="var(--plum)"/></svg>
      <span>27 Kelso Street, #14-09<br>Harbourline Tower, Singapore 058217</span>
    </li>
  </ul>

  <ul class="contact contact--online">
    <li>
      <svg viewBox="0 0 16 16" aria-hidden="true"><circle cx="8" cy="8" r="8" fill="var(--plum)"/><rect x="4" y="5.2" width="8" height="5.6" rx=".6" fill="#fff"/><path d="M4.3 5.6L8 8.4l3.7-2.8" stroke="var(--plum)" stroke-width=".9" fill="none"/></svg>
      melba@kalveria.com.sg
    </li>
    <li>
      <svg viewBox="0 0 16 16" aria-hidden="true"><circle cx="8" cy="8" r="8" fill="var(--plum)"/><g stroke="#fff" stroke-width=".9" fill="none"><circle cx="8" cy="8" r="4"/><ellipse cx="8" cy="8" rx="1.8" ry="4"/><path d="M4 8h8"/></g></svg>
      www.kalveria.com.sg
    </li>
  </ul>
</section>

</body>
</html>
```